58 Restaurant & Bar Menu

Want to make current menu more trendy in design. I have attached a pdf of the menu and of the logo. Rather, than being 6 pages I would like to make the menu into "4 pages". The menu will be printed in color.

I am open to designs that will allow the menu to be printed on 11x17 paper that will be folded in half. The "Breakfast" section needs to be its own page and all the way on the back.

As for the cover I am open to just keeping it as a cover with the info I have on it but completely different design/picture change. The logo needs to stay. The cover can also be used as having menu items on there if pulled of correctly.

The readability has to be clear to the guests.

The restaurant is a Mediterranean style and for the area it is priced mid-high. The atmosphere is casual fine dining with Martini & Wine Bar. All are ingredients are fresh never frozen and everything is prepared from scratch.

Industry/Entity Type

Restaurant

Requirements
Must have
• Breakfast on its own page on the back.
Nice to have
• Trendy Design

```html
<!DOCTYPE html>
<html lang="en">
<head>
<meta charset="utf-8">
<title>58 Restaurant &amp; Bar — Breakfast Menu</title>
<link href="https://fonts.googleapis.com/css2?family=Roboto+Condensed:wght@300;400;700&family=Roboto:wght@300;400;700&display=swap" rel="stylesheet">
<style>
  :root{
    --ink:#1c1c1c;
    --rule:#3a3a3a;
    --blue:#1aa0dc;
    --band-blue:#1d9be0;
    --band-grey:#3b4750;
    --paper:#ffffff;
    --frame:#000000;
  }
  html,body{margin:0;padding:0;width:1200px;height:804px;overflow:hidden;background:var(--frame);}
  .stage{position:absolute;left:0;top:0;width:1300px;height:871px;transform:scale(0.923077);transform-origin:0 0;background:var(--frame);font-family:"Roboto Condensed",Arial,sans-serif;color:var(--ink);}
  .page{position:absolute;top:38px;height:792px;}
  .menu-page{left:38px;width:612px;background:var(--paper);}
  .cover-page{left:650px;width:611px;overflow:hidden;}

  .col{position:absolute;top:0;}
  .col-left{left:54px;width:231px;}
  .col-mid{left:324px;width:234px;}
  .col-divider{position:absolute;left:306px;top:34px;width:1px;height:723px;background:var(--rule);}

  .hero{position:absolute;left:54px;top:2px;width:231px;height:230px;}
  .hero-photo{position:absolute;inset:0 0 30px 0;background:linear-gradient(160deg,#f3efe6 0%,#e8dcc4 35%,#c98a3f 55%,#f2d35a 70%,#ece9e2 100%);}
  .hero-title{position:absolute;left:8px;top:32px;margin:0;font-family:"Roboto",Arial,sans-serif;font-weight:300;font-size:19px;letter-spacing:6px;color:var(--blue);}
  .hero-caption{position:absolute;left:0;bottom:12px;width:100%;height:18px;background:var(--paper);font-size:12px;line-height:18px;padding-left:8px;box-sizing:border-box;}
  .hero-base{position:absolute;left:0;bottom:0;width:100%;height:12px;background:linear-gradient(90deg,#3a2a22,#6b4c38);}

  .section{position:absolute;left:0;width:100%;}
  .section-title{margin:0 0 9px;font-family:"Roboto",Arial,sans-serif;font-weight:400;font-size:11.5px;letter-spacing:2.4px;color:var(--blue);text-transform:uppercase;line-height:14px;}
  .section-note{margin:-8px 0 9px;font-size:8.5px;font-weight:400;}
  .item{display:flex;justify-content:space-between;align-items:flex-start;border-bottom:1px solid var(--rule);padding:2px 0 4px;margin-bottom:4px;}
  .item-body{flex:1;}
  .item-name{font-size:9.5px;line-height:12px;font-weight:400;}
  .item-desc{font-size:7.6px;line-height:10px;margin-top:1px;font-weight:400;}
  .item-price{font-size:9.5px;line-height:12px;text-align:right;white-space:nowrap;padding-left:8px;font-weight:400;}
  .item.is-featured .item-name,.item.is-featured .item-desc,.item.is-featured .item-price{color:var(--blue);}
  .item-lines{flex:1;}
  .item-line{display:flex;justify-content:space-between;font-size:9px;line-height:14px;font-weight:400;}
  .item-line.is-sub{padding-left:18px;font-size:8.6px;}
  .item-line.is-sub::before{content:"•";position:absolute;margin-left:-9px;}
  .item.spaced{padding-bottom:14px;}

  .cover-photo{position:absolute;inset:0;background:radial-gradient(circle at 70% 45%,#f0c44a 0%,#e2a93a 18%,transparent 40%),radial-gradient(circle at 40% 70%,#3f8a3a 0%,#2f6b2c 25%,transparent 50%),radial-gradient(circle at 25% 55%,#d8402e 0%,transparent 18%),linear-gradient(135deg,#b8b4a8 0%,#6e6a5c 30%,#3e6a30 60%,#d9d4c8 100%);}
  .brand-box{position:absolute;left:343px;top:2px;width:216px;height:132px;background:var(--paper);display:flex;align-items:center;justify-content:center;gap:8px;}
  .brand-mark{width:10px;height:10px;border-radius:50%;background:var(--blue);flex:none;}
  .brand-name{font-family:"Roboto",Arial,sans-serif;font-weight:400;font-size:17px;color:var(--ink);white-space:nowrap;}
  .info-band{position:absolute;left:0;top:664px;width:100%;height:70px;background:var(--band-blue);color:#fff;padding:28px 0 0 64px;box-sizing:border-box;clip-path:polygon(0 4px,100% 0,100% 100%,0 100%);}
  .info-lead{font-weight:700;font-size:13px;line-height:16px;letter-spacing:.3px;}
  .info-extras{font-family:"Roboto",Arial,sans-serif;font-weight:300;font-size:12.5px;line-height:18px;}
  .web-band{position:absolute;left:0;top:734px;width:100%;height:28px;background:var(--band-grey);color:#fff;font-weight:700;font-size:17px;line-height:28px;padding-left:64px;box-sizing:border-box;letter-spacing:.6px;}
  .address-band{position:absolute;left:0;top:762px;width:100%;height:30px;background:var(--band-blue);color:#fff;font-family:"Roboto",Arial,sans-serif;font-weight:300;font-size:13px;line-height:30px;padding-left:64px;box-sizing:border-box;}
  .address-band .phone{margin-left:22px;}
</style>
</head>
<body>
<div class="stage">

  <section class="page menu-page">
    <div class="hero">
      <div class="hero-photo" role="img" aria-label="Photo of a breakfast plate with sausage links, fried eggs and home fries"></div>
      <h1 class="hero-title">BREAKFAST</h1>
      <div class="hero-caption">Served Saturday &amp; Sunday</div>
      <div class="hero-base"></div>
    </div>

    <div class="col col-left">
      <div class="section" style="top:244px;">
        <h2 class="section-title">Skillets</h2>
        <div class="item"><div class="item-body"><div class="item-name">Veggie</div><div class="item-desc">Skillet full of hash browns, onions, peppers, tomatoes<br>&amp; mushrooms topped with cheese and 2 eggs.<br>Served with toast.</div></div><div class="item-price">$6.95</div></div>
        <div class="item"><div class="item-body"><div class="item-name">Irish</div><div class="item-desc">Skillet full of hash browns, onions, peppers &amp;<br>mushrooms topped with cheese and 2 eggs.<br>Served with toast.</div></div><div class="item-price">$7.95</div></div>
        <div class="item"><div class="item-body"><div class="item-name">Melting Pot</div><div class="item-desc">Skillet full of hash browns, ham, bacon, sausage,<br>mushrooms, onions, tomatoes and peppers topped<br>with cheese and 2 eggs. Served with toast.</div></div><div class="item-price">$8.95</div></div>
        <div class="item is-featured spaced"><div class="item-body"><div class="item-name">Biscuits &amp; Gravy</div><div class="item-desc">Skillet full of hash browns, onions, peppers &amp; cheese.<br>Topped with homemade biscuit, sausage gravy &amp; 2 eggs.</div></div><div class="item-price">$7.95</div></div>
      </div>

      <div class="section" style="top:499px;">
        <h2 class="section-title">Omelettes</h2>
        <p class="section-note">Fluffy Pan-Fried Omelettes, Served with Hash Browns &amp;Toast</p>
        <div class="item"><div class="item-body"><div class="item-name">Athenian</div><div class="item-desc">Gyro off-the-cone, tomatoes, onions, olives, &amp; feta<br>cheese. Served with side of homemade cucumber sauce.</div></div><div class="item-price">$8.95</div></div>
        <div class="item"><div class="item-body"><div class="item-name">Denver</div><div class="item-desc">Ham, onion, pepper &amp; cheese.</div></div><div class="item-price">$7.95</div></div>
        <div class="item"><div class="item-body"><div class="item-name">Veggie</div><div class="item-desc">Onions, peppers, tomatoes &amp; mushrooms</div></div><div class="item-price">$7.95</div></div>
        <div class="item"><div class="item-body"><div class="item-name">Deluxe</div><div class="item-desc">Ham, bacon, sausage, mushrooms, onions,<br>tomatoes &amp; peppers.</div></div><div class="item-price">$8.95</div></div>
        <div class="item is-featured"><div class="item-body"><div class="item-name">Spinach Pesto</div><div class="item-desc">Sun-Dried tomatoes, spinach, mushrooms &amp; cheese.<br>Topped with Pesto Cream Sauce.</div></div><div class="item-price">$8.95</div></div>
        <div class="item"><div class="item-body"><div class="item-name">Ham &amp; Cheese</div></div><div class="item-price">$6.95</div></div>
      </div>
    </div>

    <div class="col-divider"></div>

    <div class="col col-mid">
      <div class="section" style="top:34px;">
        <h2 class="section-title">Light Breakfast</h2>
        <div class="item"><div class="item-body"><div class="item-name">Egg, Sausage, &amp; Cheese Sand.</div></div><div class="item-price">$4.25</div></div>
        <div class="item"><div class="item-body"><div class="item-name">Oatmeal or Cereal</div></div><div class="item-price">$3.55<br>with raisins $3.95</div></div>
        <div class="item"><div class="item-body"><div class="item-name">Bagel with cream cheese</div></div><div class="item-price">$2.55</div></div>
        <div class="item"><div class="item-body"><div class="item-name">English Muffin or Raisin Toast</div></div><div class="item-price">$1.55</div></div>
        <div class="item is-featured"><div class="item-body"><div class="item-name">Mediterranean Pita</div><div class="item-desc">Pesto Spread on Pita Bread<br>with tomatoes, spinach, feta &amp; an Egg.</div></div><div class="item-price">$6.95</div></div>
        <div class="item"><div class="item-body"><div class="item-name">Fresh Fruit Bowl</div></div><div class="item-price">$4.95</div></div>
      </div>

      <div class="section" style="top:244px;">
        <h2 class="section-title">Eggs &amp; Specialties</h2>
        <div class="item spaced"><div class="item-lines">
          <div class="item-line"><span>Two Eggs, Hash Browns &amp; Toast</span><span>$4.95</span></div>
          <div class="item-line is-sub"><span>With Bacon, Sausage or Ham</span><span>$5.95</span></div>
          <div class="item-line is-sub"><span>With Corned Beef Hash</span><span>$6.55</span></div>
          <div class="item-line is-sub"><span>With Gyro off-the-cone</span><span>$6.95</span></div>
        </div></div>
        <div class="item spaced"><div class="item-body"><div class="item-name">Steak &amp; Eggs</div><div class="item-desc">8oz Prime Cut Steak, 2 Eggs, hash browns, &amp; Toast.</div></div><div class="item-price">$13.95</div></div>
        <div class="item spaced"><div class="item-body"><div class="item-name">Chop Steak &amp; Eggs</div><div class="item-desc">10oz Chopped Sirloin Steak, 2 Eggs, hash browns, &amp; Toast.</div></div><div class="item-price">$9.95</div></div>
        <div class="item spaced"><div class="item-body"><div class="item-name">Granny’s Breakfast</div><div class="item-desc">Two Eggs scrambled with potatoes, ham, onions &amp;<br>peppers topped with cheese. Served with toast.</div></div><div class="item-price">$6.95</div></div>
        <div class="item"><div class="item-body"><div class="item-name">3 Deuces</div><div class="item-desc">Two Eggs, Two Pancakes &amp;<br>Two Sausage Links or Bacon Strips.</div></div><div class="item-price">$6.95</div></div>
        <div class="item"><div class="item-body"><div class="item-name">Homemade Biscuits &amp; Gravy</div></div><div class="item-price">Half $3.95<br>Full $5.55</div></div>
      </div>

      <div class="section" style="top:586px;">
        <h2 class="section-title">Pancakes,<br>French Toast &amp; Waffles</h2>
        <div class="item"><div class="item-body"><div class="item-name">Apple Danish French Toast</div></div><div class="item-price">$6.95</div></div>
        <div class="item"><div class="item-body"><div class="item-name">Bananas Foster Pancakes</div></div><div class="item-price">$7.95</div></div>
        <div class="item"><div class="item-body"><div class="item-name">Strawberry Cake Waffle</div></div><div class="item-price">$7.95</div></div>
        <div class="item"><div class="item-body"><div class="item-name">Pancakes or French Toast</div></div><div class="item-price">(2) $4.55<br>(3) $4.95</div></div>
        <div class="item"><div class="item-lines">
          <div class="item-line"><span>Belgium Waffle</span><span>$4.95</span></div>
          <div class="item-line is-sub"><span>Add Fruit Topping, Bacon, Ham or Sausage</span><span>$1.95</span></div>
        </div></div>
      </div>
    </div>
  </section>

  <section class="page cover-page">
    <div class="cover-photo" role="img" aria-label="Close-up photo of a Mediterranean salad with grilled chicken, spinach, tomatoes, cucumber, olives and feta"></div>
    <div class="brand-box">
      <span class="brand-mark"></span>
      <span class="brand-name">58 Restaurant &amp; Bar</span>
    </div>
    <div class="info-band">
      <div class="info-lead">Serving Breakfast Saturday &amp; Sunday</div>
      <div class="info-extras">Catering &amp; Private Party Hosting Available • Friday Fish Fry • Saturday Prime Rib</div>
    </div>
    <div class="web-band">www.58restaurantbar.com</div>
    <div class="address-band">58 N Harbor St · Lakeview, WI 53000<span class="phone">262-555-0148</span></div>
  </section>

</div>
</body>
</html>
```